Label Design for RTD Cocktail Line Tolvanu Cellars

Tolvanu Cellars is a line of Indian-inspired artisan cocktails that "brings the bartender home" for professional men and women who like the finer things in life but don’t always have the time to treat themselves. No need for a multitude of expensive and hard-to-find ingredients, time consuming recipes, or a mixologist.

Our line of 3 open and serve cocktails blends a range of premium spirits with exotic ingredients so you can conveniently raise a glass for any of life’s celebrations.

Our bottle is the 750ml Claret bottle with Quorlex (screw cap) closure and will be covered entirely in a shrink sleeve (so potentially anything can be designed for any part of the bottle). We want the bottle to pop on the shelf so it should look different than what’s already out there (Velvet Fawn, Korvadel, Mirelda ready to drink cocktails). We are looking for a sexy design that's polished/sleek.
Updates

Reason: Hello designers! Tolvanu Cellars is so impressed with what we have received thus far and we would like to give some of the designers a few extra days to make the edits we requested. It's never too late to submit! Thank you all!

Requirements
Must have
• Front of bottle
* “Tolvanu Cellars” name and Peacock Logo- but feel free to pull the elements apart and use them on the bottle in different ways
* Open & Serve
* 12% ALC/VOL
* 750 ml
* 3 different labels in a theme for
-Brovanza
-Zestrovino
-Florquena

Brovanza Ideas- soft brown palate, the ingredients in chai spice (cloves, cardamom pods, nutmeg, black peppercorns, star anise, and cinnamon stick)

Zestrovino Ideas -cool and refreshing, pale green shade (not clashing with logo), graphics of fresh mint leaves, green chili, lime, cucumber

Florquena Ideas- soft/pale pink shades, graphics of lychi fruit (outer red shell and inner pink flesh), ginger

Back of bottle
* explanation of the 3 cocktails
Brovanza: Forget what you think you know about chai, this is not the Queen’s tea-time drink! Brovanza is a smooth, sweetly -spiced cocktail made with vodka, black tea, and a combination of aromatic spices. This velvety cocktail is rich without being heavy. Enjoy chilled or over ice anytime.

Zestrovino: Zestrovino can’t make up its mind! This fusion of zesty lime, sweet mint, earthy cucumber and spicy chilies is so refreshing you’ll crave it on a hot summer day or a cool winter’s night. The exotic botanicals in gin add a complexity to the cocktail making this a refreshing but potent drink! Enjoy chilled or over ice anytime.

Florquena: East meet West. Delicate lychi meet hard-hitting whiskey. Florquena will tempt you senses with flavor, fragrance and beauty. The peppery kick of ginger and the intensity of the un-aged whiskey are softened by lychi’s intoxicating scent and subtle, sweet finish.

Please include
1. Bottled By PQR Spirits Company
2. Sample barcode (where you would place it in your design)
3. www.TolvanuCellars.example
4. GOVERNMENT WARNING: (1) According to the Surgeon General, women should not drink alcoholic beverages during pregnancy because of the risk of birth defects. (2) Consumption of alcoholic beverages impairs your ability to drive a car or operate machinery, and may cause health problems.

Optional to include
*"Bring the Bartender Home"
*"Tolvanu Cellars” name and Peacock Logo on the back
*Entirely black sleeve with contrasting design

FYI the Fonts used in our logo are Geosans Light and Prakrta, but feel free to use other complimentary fonts on the other aspects.
Nice to have
• Optional to include

```html
<!DOCTYPE html>
<html lang="en">
<head>
<meta charset="utf-8">
<title>Zestrovino – Tolvanu Cellars Sleeve</title>
<link rel="stylesheet" href="https://fonts.googleapis.com/css2?family=Jost:wght@300;400&family=Courier+Prime:wght@400;700&display=swap">
<style>
  :root {
    --stage: #6f8399;
    --sleeve: #050807;
    --capsule: #5f9a6a;
    --capsule-text: #1d3a24;
    --title-blue: #3aa9dc;
    --mint-light: #8fe3b4;
    --mint: #5fcf92;
    --mint-deep: #2a8f63;
    --ink-light: #e8eef0;
    --ink-muted: #b9c4c6;
    --code-box: #f4f6f5;
  }
  * { box-sizing: border-box; margin: 0; padding: 0; }
  html, body { width: 1200px; height: 1000px; overflow: hidden; }
  body {
    background: var(--stage);
    font-family: "Jost", sans-serif;
    font-weight: 300;
    color: var(--ink-light);
    position: relative;
  }
  .sleeve-panel {
    position: absolute;
    top: 50px;
    width: 440px;
    height: 900px;
    background: var(--sleeve);
    overflow: hidden;
  }
  .sleeve-panel--front { left: 130px; }
  .sleeve-panel--back { left: 630px; }

  .neck-capsule {
    height: 90px;
    background: var(--capsule);
    display: flex;
    align-items: flex-end;
    justify-content: center;
    padding-bottom: 14px;
  }
  .neck-capsule__name {
    font-size: 15px;
    font-weight: 300;
    letter-spacing: 4px;
    color: var(--capsule-text);
    text-transform: uppercase;
  }

  /* Front */
  .product-title {
    font-size: 38px;
    font-weight: 300;
    letter-spacing: 8px;
    color: var(--title-blue);
    text-align: center;
    margin-top: 150px;
    text-transform: uppercase;
  }
  .product-type {
    text-align: center;
    font-size: 15px;
    margin-top: 10px;
  }
  .botanical-art {
    position: absolute;
    left: 30px;
    top: 330px;
    width: 290px;
    height: 420px;
    border-radius: 18px;
    background:
      radial-gradient(ellipse at 62% 28%, var(--mint-light) 0%, var(--mint) 30%, rgba(42,143,99,0) 60%),
      radial-gradient(ellipse at 30% 60%, var(--mint) 0%, var(--mint-deep) 40%, rgba(5,8,7,0) 75%),
      radial-gradient(ellipse at 55% 88%, var(--mint-deep) 0%, rgba(5,8,7,0) 65%);
  }
  .front-footer {
    position: absolute;
    left: 0; right: 0; bottom: 44px;
    padding: 0 40px;
    display: flex;
    justify-content: space-between;
    align-items: flex-end;
  }
  .serve-note { font-size: 13px; }
  .front-meta { text-align: right; font-size: 13px; line-height: 1.4; }
  .brand-mark {
    display: flex;
    align-items: center;
    gap: 6px;
    justify-content: flex-end;
    margin-bottom: 10px;
    color: var(--title-blue);
    font-size: 14px;
    font-weight: 300;
  }
  .brand-mark__dot {
    width: 12px; height: 12px;
    border-radius: 50%;
    background: var(--title-blue);
  }

  /* Back */
  .back-brand {
    display: flex;
    flex-direction: column;
    align-items: center;
    margin-top: 110px;
    gap: 8px;
  }
  .back-brand__dot {
    width: 34px; height: 34px;
    border-radius: 50%;
    background: var(--title-blue);
  }
  .back-brand__name {
    font-size: 26px;
    font-weight: 300;
    color: var(--title-blue);
    letter-spacing: 1px;
  }
  .tagline {
    text-align: center;
    font-size: 15px;
    margin-top: 12px;
  }
  .back-title {
    font-size: 36px;
    font-weight: 300;
    letter-spacing: 8px;
    color: var(--title-blue);
    text-align: center;
    margin-top: 32px;
    text-transform: uppercase;
  }
  .story {
    font-size: 12.5px;
    line-height: 1.5;
    padding: 0 44px;
    margin-top: 14px;
  }
  .web-address {
    padding: 0 44px;
    margin-top: 10px;
    font-size: 11px;
    letter-spacing: 2px;
    color: var(--title-blue);
    text-transform: uppercase;
  }
  .gov-warning {
    font-family: "Courier Prime", monospace;
    font-size: 10.5px;
    line-height: 1.4;
    padding: 0 44px;
    margin-top: 36px;
    color: var(--ink-muted);
  }
  .gov-warning strong { font-weight: 700; }
  .back-footer {
    position: absolute;
    left: 44px; right: 44px; bottom: 40px;
    display: flex;
    align-items: flex-end;
    justify-content: space-between;
    gap: 16px;
  }
  .barcode-slot {
    display: flex;
    flex-direction: column;
    align-items: center;
    gap: 4px;
  }
  .barcode-slot__area {
    width: 120px;
    height: 52px;
    background: var(--code-box);
    border-radius: 2px;
  }
  .barcode-slot__label {
    font-size: 10px;
    letter-spacing: 2px;
    color: var(--ink-light);
    text-transform: uppercase;
  }
  .back-footer__notes {
    text-align: right;
    font-size: 11px;
    line-height: 1.9;
    color: var(--ink-muted);
  }
</style>
</head>
<body>

  <section class="sleeve-panel sleeve-panel--front">
    <div class="neck-capsule"></div>
    <h1 class="product-title">Zestrovino</h1>
    <p class="product-type">A Gin Cocktail</p>
    <div class="botanical-art" role="img" aria-label="Mint green line illustration of a green chili, a cucumber slice, a lime half and mint leaves"></div>
    <div class="front-footer">
      <p class="serve-note">Open &amp; Serve</p>
      <div class="front-meta">
        <div class="brand-mark"><span class="brand-mark__dot"></span>Tolvanu Cellars</div>
        <p>12% ALC/VOL</p>
        <p>750 ml</p>
      </div>
    </div>
  </section>

  <section class="sleeve-panel sleeve-panel--back">
    <div class="neck-capsule"><span class="neck-capsule__name">Zestrovino</span></div>
    <div class="back-brand">
      <span class="back-brand__dot"></span>
      <span class="back-brand__name">Tolvanu Cellars</span>
    </div>
    <p class="tagline">Bring the Bartender Home</p>
    <h2 class="back-title">Zestrovino</h2>
    <p class="story">Zestrovino can’t make up its mind! This fusion of zesty lime, sweet mint, earthy cucumber and spicy chilies is so refreshing you’ll crave it on a hot summer day or a cool winter’s night. The exotic botanicals in gin add a complexity to the cocktail making this a refreshing but potent drink! Enjoy chilled or over ice anytime.</p>
    <p class="web-address">www.TolvanuCellars.example</p>
    <p class="gov-warning"><strong>GOVERNMENT WARNING:</strong> (1) According to the Surgeon General, women should not drink alcoholic beverages during pregnancy because of the risk of birth defects. (2) Consumption of alcoholic beverages impairs your ability to drive a car or operate machinery, and may cause health problems.</p>
    <div class="back-footer">
      <div class="barcode-slot" role="img" aria-label="Space reserved for the product barcode">
        <div class="barcode-slot__area"></div>
        <span class="barcode-slot__label">Barcode</span>
      </div>
      <div class="back-footer__notes">
        <p>Contains FD&amp;C Yellow #5</p>
        <p>Bottled By PQR Spirits Company</p>
      </div>
    </div>
  </section>

</body>
</html>
```